Environmental Consultancey needs Web Design

A consultancey firm based in Papua New Guinea specialising servicing a client market primarily in Melanesia, the wider Pacific Region and South East Asia. The firm provides services to community development and resource extraction activites that incorporate sustainable livelihoods for local customary land owners with environmentally responsibile practices and a focus on maintaining biodiversity and ecosystem services. We aim to encompass Culture, Custom and Science in our approach. Our website preferentially will convey a relaxed Pacific Island feel in its colours and design rather than a sterile corporate feel. See attached logo that will need to be visible on page or which may provide basis for ideas for the page.

Target Market(s)

Our target market is primarily the oil, gas and mining industry, secondarily international donor and aid programs followed by government projects and not for profit programs. Services include:
1. Biodiversity and Conservation - Fauna and Flora survey, assessment, management, monitoring & research, protected areas & endangered & threatend species.
2. Social & Community - impact, stakeholder engagement, census and survey, land and community affairs, capacity building empowerment.
3. Environmental Management - sustainable use, enterprise development & management, biodiversity offsets.

Industry/Entity Type

Community

Requirements
Must have
• Multiple pages, Logo somewhere on home page. Space for a couple of photos that as yet ive not decieded upon.
Nice to have
• Perhaps incorporate shapes, texture and colours that convey a feel of the attached photo of a blue bird of paradise. The blue fine overlapping and interlocking feather patterns are appealing perhaps as a background and the other colours used in boarders ? Abstract is fine as would be symbolic images or tribal ambience. The company is all about blending humanity in all its forms with the environment.

```html
<!DOCTYPE html>
<html lang="en">
<head>
<meta charset="utf-8">
<title>Palmleaf Environs</title>
<link href="https://fonts.googleapis.com/css2?family=Ubuntu:ital,wght@0,400;0,500;0,700;1,700&family=Ubuntu+Condensed&family=Open+Sans:wght@400;700&display=swap" rel="stylesheet">
<style>
:root{
  --green:#1f8d3b;
  --green-dark:#137030;
  --green-deep:#0f6a2a;
  --yellow:#f3e31c;
  --yellow-light:#fbf6a8;
  --red:#c8161b;
  --teal:#2b5e5e;
  --panel:#4b6866;
  --cyan:#2fc0e0;
  --cyan-light:#52d4ef;
  --orange:#e8b25a;
  --orange-light:#f6d38f;
  --ink:#222;
  --grey:#666;
  --footer:#231f20;
  --field:#505050;
  --white:#fff;
}
*{box-sizing:border-box;margin:0;padding:0}
html,body{width:993px;height:1200px;overflow:hidden;background:var(--white)}
body{position:relative;font-family:'Open Sans',sans-serif;color:var(--ink)}
.abs{position:absolute}
.heading{font-family:'Ubuntu',sans-serif;font-weight:400}

/* header */
.header-band{left:0;top:0;width:993px;height:150px}
.brand{left:112px;top:8px;width:148px;height:125px;background:var(--white);display:flex;flex-direction:column;align-items:center;justify-content:center;gap:8px}
.brand-mark{width:44px;height:44px;border-radius:50%;background:var(--green)}
.brand-name{font-family:'Ubuntu',sans-serif;font-size:15px;color:var(--green-dark);text-align:center;line-height:1.15}
.follow{left:712px;top:24px;font-size:12px;color:#555}
.social{top:17px;width:28px;height:28px;border-radius:50%;background:#3d8fd0;border:2px solid #e4eef7}
.search-tab{left:688px;top:76px;width:197px;height:36px;background:var(--green-deep);border-radius:0 0 6px 6px}
.search{left:703px;top:82px;width:176px;height:22px;border-radius:11px;background:linear-gradient(#fff,#d8d8d8);border:1px solid #bbb;font-size:11px;font-style:italic;color:#555;padding:3px 0 0 13px}
.search svg{position:absolute;right:5px;top:2px}

/* nav */
.nav{left:0;top:147px;width:993px;height:34px;background:linear-gradient(var(--yellow-light) 0%,var(--yellow) 45%,#e9d400 100%);border-bottom:1px solid #c6b400}
.nav a{position:absolute;top:0;height:33px;line-height:33px;font-family:'Ubuntu',sans-serif;font-size:14px;color:#2a2a1a;text-decoration:none}
.nav a.active{background:linear-gradient(#e2262b,var(--red));color:var(--white);padding:0 18px;border-radius:3px 3px 0 0}

/* hero */
.hero-bg{left:0;top:181px;width:993px;height:321px;background:linear-gradient(90deg,#16782f,#2aa547 30%,#1f8d3b 60%,#138034)}
.hero-frame{left:108px;top:182px;width:779px;height:294px;background:var(--white);box-shadow:0 2px 6px rgba(0,0,0,.35)}
.hero-photo{left:113px;top:187px;width:769px;height:284px;background:radial-gradient(circle at 300px 150px,#3a8fd6 0,#4ea3d8 40px,#c9e36a 95px,#86c23a 200px,#4d8d22 420px)}
.hero-caption{left:113px;top:415px;width:560px;height:56px;background:rgba(25,25,25,.85);color:var(--white);font-family:'Ubuntu Condensed',sans-serif;font-size:27px;padding:10px 0 0 15px}
.slide{left:643px;width:239px;height:56px}
.slide svg{position:absolute;left:0;top:0}
.slide-title{position:absolute;left:37px;top:4px;font-family:'Ubuntu',sans-serif;font-weight:500;font-size:16px;color:#111}
.slide-text{position:absolute;left:37px;top:22px;width:190px;font-size:10px;line-height:13px;color:#134;text-align:justify}

/* content */
.welcome-title{left:108px;top:519px;font-size:22px;color:var(--teal)}
.welcome-text{left:108px;top:548px;width:513px;font-size:10.7px;line-height:20px;color:var(--grey);text-align:justify}
.btn{border-radius:5px;background:linear-gradient(var(--orange-light),var(--orange));border:1px solid #caa057;font-family:'Ubuntu',sans-serif;color:#222;text-align:center}
.read-more{left:554px;top:643px;width:67px;height:28px;line-height:27px;font-size:12px}
.projects-title{left:108px;top:676px;font-size:21px;color:var(--teal)}
.project-main{left:108px;top:708px;width:447px;height:162px;border-radius:4px;background:linear-gradient(120deg,#1f8fc8,#3ab0e6 45%,#5a8fb8 70%,#c9b98c)}
.thumb{top:877px;width:107px;height:54px;border-radius:4px}
.thumb.blue{background:linear-gradient(120deg,#2494c8,#4ab3e0 60%,#c8c08e)}
.thumb.green{background:linear-gradient(120deg,#8a8a3a,#2e8b6e 50%,#e6dcb0)}

/* news */
.news{left:637px;top:525px;width:248px;height:272px;background:var(--panel);border-radius:4px;color:var(--white)}
.news-title{position:absolute;left:16px;top:6px;font-size:21px}
.news-item{position:absolute;left:10px;width:224px;height:78px}
.news-item.divided{border-bottom:1px solid #7a9290}
.news-date{position:absolute;left:0;top:6px;width:48px;text-align:center;font-family:'Ubuntu',sans-serif;font-style:italic;font-weight:700;font-size:19px;line-height:21px;color:#dfe6e4}
.news-text{position:absolute;left:56px;top:5px;width:170px;font-size:10.5px;line-height:13px}
.news-text b{color:var(--orange-light);text-decoration:underline;font-weight:700}
.news-more{position:absolute;right:0;top:44px;font-size:10.5px;font-style:italic;font-weight:700;color:var(--orange-light);text-decoration:underline}
.signup-title{left:636px;top:806px;font-size:21px;color:var(--teal)}
.signup-text{left:637px;top:833px;width:250px;font-size:10.5px;line-height:13.5px;color:var(--grey)}
.signup-field{left:637px;top:870px;width:248px;height:24px;border-radius:4px;background:linear-gradient(#c8c8c8,#f4f4f4);border:1px solid #aaa}
.sign-in{left:818px;top:903px;width:67px;height:27px;line-height:26px;font-size:12px}

/* footer */
.footer{left:0;top:950px;width:993px;height:250px;background:var(--footer);color:#ddd}
.footer-title{position:absolute;top:15px;font-size:17px;color:var(--white)}
.quick-links{position:absolute;left:108px;top:38px;list-style:none;font-size:10.5px;line-height:20px}
.quick-links li{text-decoration:underline;color:#ddd}
.field{position:absolute;left:306px;width:248px;height:23px;border-radius:4px;background:var(--field);border:1px solid #888;font-size:10.5px;color:#bbb;padding:4px 0 0 10px}
.submit{position:absolute;left:488px;top:198px;width:66px;height:27px;line-height:26px;font-size:14px}
.contact{position:absolute;left:639px;top:40px;font-size:10.5px;line-height:15px;color:#ddd}
.contact b{color:var(--white)}
.copyright{position:absolute;right:107px;top:196px;text-align:right;font-size:10.5px;line-height:15px;font-weight:700;color:#ccc;text-decoration:underline}
</style>
</head>
<body>

<svg class="abs header-band" viewBox="0 0 993 150" aria-hidden="true">
  <polygon points="0,147 0,145 260,128 993,42 993,150 0,150" fill="#1f8d3b"/>
</svg>

<div class="abs brand">
  <div class="brand-mark"></div>
  <div class="brand-name">Palmleaf<br>Environs</div>
</div>

<div class="abs follow">Follow us on :</div>
<div class="abs social" style="left:792px"></div>
<div class="abs social" style="left:825px"></div>
<div class="abs social" style="left:858px"></div>

<div class="abs search-tab"></div>
<div class="abs search">Search
  <svg width="22" height="18" viewBox="0 0 22 18" aria-hidden="true"><circle cx="8" cy="7" r="5" fill="none" stroke="#222" stroke-width="2"/><line x1="12" y1="11" x2="19" y2="16" stroke="#222" stroke-width="3"/></svg>
</div>

<nav class="abs nav">
  <a class="active" style="left:228px">Home</a>
  <a style="left:313px">About Us</a>
  <a style="left:397px">Our Projects</a>
  <a style="left:501px">Our Services</a>
  <a style="left:611px">Safety Tips</a>
  <a style="left:711px">Latest News</a>
  <a style="left:818px">Contact Us</a>
</nav>

<div class="abs hero-bg" role="img" aria-label="Green rainforest texture background"></div>
<div class="abs hero-frame"></div>
<div class="abs hero-photo" role="img" aria-label="Hand holding a small globe among green leaves"></div>
<div class="abs hero-caption">"Encompassing Culture, Custom &amp; Science"</div>

<div class="abs slide" style="top:184px"><svg width="239" height="56"><polygon points="0,0 239,0 239,55 22,55" fill="#2fc0e0"/></svg><div class="slide-title">Slide 1</div><div class="slide-text">Nemo enim ipsam voluptatem quia voluptas</div></div>
<div class="abs slide" style="top:240px"><svg width="239" height="58"><polygon points="0,0 239,0 239,57 22,57" fill="#3ac7e5"/></svg><div class="slide-title">Slide 2</div><div class="slide-text">Nemo enim ipsam voluptatem quia voluptas</div></div>
<div class="abs slide" style="top:298px"><svg width="239" height="58"><polygon points="0,0 239,0 239,57 22,57" fill="#2fc0e0"/></svg><div class="slide-title">Slide 3</div><div class="slide-text">Nemo enim ipsam voluptatem quia voluptas</div></div>
<div class="abs slide" style="top:356px"><svg width="239" height="58"><polygon points="0,0 239,0 239,57 22,57" fill="#3ac7e5"/></svg><div class="slide-title">Slide 4</div><div class="slide-text">Nemo enim ipsam voluptatem quia voluptas</div></div>
<div class="abs slide" style="top:414px"><svg width="239" height="57"><polygon points="0,0 239,0 239,57 22,57" fill="#2fc0e0"/></svg><div class="slide-title">Slide 5</div><div class="slide-text">Nemo enim ipsam voluptatem quia voluptas</div></div>

<h1 class="abs heading welcome-title">Welcome to Our Site !</h1>
<p class="abs welcome-text">Nemo enim ipsam voluptatem quia voluptas sit aspernatur aut odit aut fugit, sed quia consequuntur magni dolores eos qui ratione voluptatem sequi nesciunt. Neque porro quisquam est. Sed ut perspiciatis unde omnis iste natus error sit voluptatem accusantium doloremque laudantium, totam rem aperiam, eaque ipsa quae ab illo inventore veritatis et quasi architecto beatae vitae dicta.</p>
<div class="abs btn read-more">Read More</div>

<h2 class="abs heading projects-title">Our Projects</h2>
<div class="abs project-main" role="img" aria-label="Blue bird perched on a branch"></div>
<div class="abs thumb blue" style="left:108px" role="img" aria-label="Project thumbnail: blue bird"></div>
<div class="abs thumb green" style="left:221px" role="img" aria-label="Project thumbnail: bird in foliage"></div>
<div class="abs thumb blue" style="left:334px" role="img" aria-label="Project thumbnail: blue bird"></div>
<div class="abs thumb green" style="left:447px" role="img" aria-label="Project thumbnail: bird in foliage"></div>

<aside class="abs news">
  <div class="heading news-title">Latest News</div>
  <div class="news-item divided" style="top:34px"><div class="news-date">02<br>MAR</div><div class="news-text"><b>Nemo enim ipsam</b> voluptatem quia voluptas sit aspernatur aut odit aut fugit.</div><div class="news-more">Read More</div></div>
  <div class="news-item divided" style="top:113px"><div class="news-date">29<br>FEB</div><div class="news-text"><b>Nemo enim ipsam</b> voluptatem quia voluptas sit aspernatur aut odit aut fugit.</div><div class="news-more">Read More</div></div>
  <div class="news-item" style="top:192px"><div class="news-date">27<br>FEB</div><div class="news-text"><b>Nemo enim ipsam</b> voluptatem quia voluptas sit aspernatur aut odit aut fugit.</div><div class="news-more">Read More</div></div>
</aside>

<h2 class="abs heading signup-title">SignUp Newsletter</h2>
<p class="abs signup-text">Get free updates in your mail Account, Please enter your valid Email Adderess</p>
<div class="abs signup-field"></div>
<div class="abs btn sign-in">Sign-In</div>

<footer class="abs footer">
  <div class="heading footer-title" style="left:108px">Quick Links</div>
  <ul class="quick-links">
    <li>Home</li><li>About Us</li><li>Our Projects</li><li>Our Sevices</li><li>Safety Tips</li><li>Latest News</li><li>Contact Us</li>
  </ul>
  <div class="heading footer-title" style="left:306px">Queries/Comments</div>
  <div class="field" style="top:45px">Name</div>
  <div class="field" style="top:74px">Contact No</div>
  <div class="field" style="top:102px">Email Id</div>
  <div class="field" style="top:131px;height:56px">Comments</div>
  <div class="btn submit">Submit</div>
  <div class="heading footer-title" style="left:637px">Contact Info</div>
  <div class="contact">Nemo enim ipsam<br>voluptatem quia<br>voluptas sit aspernatur<br><br><b>Phone :</b> 320 555 014<br><b>Fax :</b> 320 555 015<br><b>Email :</b> <u>info@ palmleaf.pg</u></div>
  <div class="copyright">Copyright © 2012 by Palmleaf Environs<br>All rights reserved</div>
</footer>

</body>
</html>
```